new letterhead for my brokergae company KeelBright, Complete Marine Brokerage

We need a new letterhead for our brokerage company called KeelBright. We are specialised in selling pleasure crafts (sailing and motoryachts). More info can be found at https://keelbright-example.com/en

I use this document for a quotation, a letter, sales agreement, selling instructions. I am looking for a cover page + a content page.

Th efollowing information needs to be in the header / footer; email, website, VAT number, Bank Account number, number chamber of ccomerce, registry number prav, General terms and conditions DQRT apply.

```html
<!DOCTYPE html>
<html lang="en">
<head>
<meta charset="utf-8">
<title>KeelBright Letterhead</title>
<link href="https://fonts.googleapis.com/css2?family=Roboto:wght@400;500&family=Ubuntu:wght@400;500&family=Great+Vibes&display=swap" rel="stylesheet">
<style>
  :root{
    --backdrop:#b3b3b3;
    --paper:#f5f5f5;
    --ink:#666666;
    --ink-dark:#5a5a5a;
    --footer-ink:#2b2b2b;
    --legal-ink:#7a7a7a;
    --brand:#1a5fad;
    --signature:#2d4f86;
  }
  *{margin:0;padding:0;box-sizing:border-box;}
  html,body{width:1132px;height:1200px;overflow:hidden;}
  body{background:var(--backdrop);position:relative;font-family:"Roboto",Arial,sans-serif;}
  .letterhead{
    position:absolute;left:247px;top:149px;width:637px;height:901px;
    background:var(--paper);overflow:hidden;
  }
  .brand{position:absolute;left:0;right:0;top:62px;text-align:center;}
  .brand-name{
    display:inline-flex;align-items:center;gap:10px;
    font-family:"Ubuntu",Arial,sans-serif;font-weight:500;font-size:37px;
    color:var(--brand);line-height:1;
  }
  .brand-dot{width:12px;height:12px;border-radius:50%;background:var(--brand);}
  .brand-tagline{
    margin-top:9px;font-family:"Ubuntu",Arial,sans-serif;font-weight:500;
    font-size:8.5px;letter-spacing:2.2px;color:var(--brand);text-transform:uppercase;
    padding-left:22px;
  }
  .letter{
    position:absolute;left:40px;width:557px;font-size:10.5px;line-height:14.4px;color:var(--ink);
  }
  .letter-date{top:226px;}
  .recipient{top:269px;font-style:normal;}
  .recipient strong{font-weight:500;color:var(--ink-dark);}
  .salutation{top:356px;}
  .body-copy{top:385px;}
  .body-copy p{text-align:justify;margin-bottom:14.4px;letter-spacing:-0.18px;}
  .sign-off{top:658px;}
  .sign-name{font-weight:500;color:var(--ink-dark);}
  .signature{
    position:absolute;left:28px;top:678px;font-family:"Great Vibes",cursive;
    font-size:24px;color:var(--signature);line-height:1;
  }
  .sign-role{position:absolute;left:40px;top:714px;font-size:10.5px;color:var(--ink);}
  .footer{
    position:absolute;left:0;right:0;top:824px;text-align:center;
    font-family:"Ubuntu",Arial,sans-serif;font-size:11.5px;color:var(--footer-ink);
  }
  .footer-contacts{margin-top:5px;display:flex;justify-content:center;align-items:center;gap:8px;}
  .contact-item{display:inline-flex;align-items:center;gap:4px;white-space:nowrap;}
  .contact-item svg{fill:var(--brand);}
  .web-accent{color:var(--brand);}
  .footer-legal{
    margin-top:9px;font-size:7.5px;line-height:11px;color:var(--legal-ink);
  }
</style>
</head>
<body>
  <main class="letterhead">
    <header class="brand">
      <div class="brand-name"><span class="brand-dot"></span>KeelBright</div>
      <div class="brand-tagline">Complete Marine Brokerage</div>
    </header>

    <div class="letter letter-date">30/20/2016</div>

    <address class="letter recipient">
      <strong>Mr. XYZ Smith</strong><br>
      123, Street No. 123,<br>
      City Name<br>
      Pincode-123456
    </address>

    <div class="letter salutation">Dear Sir,</div>

    <section class="letter body-copy">
      <p>Lorem Ipsum is simply dummy text of the printing and typesetting industry. Lorem Ipsum has been the industry's standard dummy text ever since the 1500s, when an unknown printer took a galley of type and scrambled it to make a type specimen book. It has survived not only five centuries, but also the leap into electronic typesetting, remaining essentially unchanged. It was popularised in the 1960s with the release of TypeSheets sheets containing Lorem Ipsum passages, and more recently with desktop publishing software like PageSetter Pro including versions of Lorem Ipsum.</p>
      <p>Lorem Ipsum is simply dummy text of the printing and typesetting industry. Lorem Ipsum has been the industry's standard dummy text ever since the 1500s, when an unknown printer took a galley of type and scrambled it to make a type specimen book. It has survived not only five centuries, but also the leap into electronic typesetting, remaining essentially unchanged. It was popularised in the 1960s with the release of TypeSheets sheets containing Lorem Ipsum passages, and more recently with desktop publishing software like PageSetter Pro including versions of Lorem Ipsum.</p>
      <p>Lorem Ipsum is simply dummy text of the printing and typesetting industry. Lorem Ipsum has been the industry's standard dummy text ever since the 1500s, when an unknown printer took a galley of type and scrambled it to make a type specimen book.</p>
    </section>

    <div class="letter sign-off"><span class="sign-name">Your Name</span></div>
    <div class="signature">Your Signature</div>
    <div class="sign-role">CEO &nbsp;|&nbsp; Owner</div>

    <footer class="footer">
      <div class="footer-address">Havenkade 12, 4811 AB Harbourtown, Netherlands</div>
      <div class="footer-contacts">
        <span class="contact-item">
          <svg width="9" height="11" viewBox="0 0 9 11" aria-hidden="true"><path d="M1 0h7v1.5H6.5v7H8V11H1V8.5h1.5v-7H1z M3.5 1.5v7h2v-7z"/></svg>
          +31 (0)85 000 12 34
        </span>
        <span class="contact-item">
          <svg width="11" height="8" viewBox="0 0 11 8" aria-hidden="true"><path d="M0 0h11v8H0z M1 1l4.5 3.5L10 1z" fill-rule="evenodd"/></svg>
          contact@keelbright-example.com
        </span>
        <span class="contact-item">
          <svg width="9" height="9" viewBox="0 0 10 10" aria-hidden="true"><circle cx="5" cy="5" r="5"/><path d="M0 5h10M5 0v10" stroke="#f5f5f5" stroke-width="0.8"/></svg>
          <span>www.<span class="web-accent">keelbright</span>-example.com</span>
        </span>
      </div>
      <div class="footer-legal">
        VAT NL000000000B01 &nbsp;|&nbsp; IBAN NL00 BANK 0000 0000 00 &nbsp;|&nbsp; Chamber of Commerce 00000000 &nbsp;|&nbsp; prav registry no. 0000<br>
        General terms and conditions DQRT apply
      </div>
    </footer>
  </main>
</body>
</html>
```